PSD website for property company

Please read the brief thoroughly.

We are looking for a new website for a property group that does property acquisitions, property development and property management.
They buy, build and lease core inner city industrial assets in Sydney, Australia.
They also invest in residential developments.

Site menu
- Home page
- Property – sub menus include – Leasing ; Projects ; Investments ; Property Management
- Capital and finance
- About
- Contact

They like this website
https://www.verlo.com.au/

They want the site to be clean, modern and bold.
They like few colors, even black and white is OK to submit

They have a logo and style guide and useable images here:
http://www.kumet.net/temp/PelorisWeb2019.zip
The zip file is also attached to this project.
We have supplied some images to give you an idea, but we will also require you to provide at least 3 extra images from stock photos.
Use your imagination.

I am expecting a lot of similar designs, so be aware the photos you choose will be really important.
They want really 3 good stock photos used and supplied without charge.
Please not too generic, I repeat the quality of the photos is important.
You may provide several photos (but not in multiple submissions please) and we will choose the best three to be provided.

The winner will be selected on a single home page design and required to provide;
All photos use in original format without charge
A second ‘standard page’ template design based on the winning home page design

```html
<!DOCTYPE html>
<html lang="en">
<head>
<meta charset="utf-8">
<title>Peloris – Footer</title>
<link rel="stylesheet" href="https://fonts.googleapis.com/css2?family=Jost:wght@300;400;500;600&display=swap">
<style>
  :root {
    --bg: #2b2b2b;
    --rule: #444444;
    --text-strong: #ffffff;
    --text-muted: #a9a9a9;
  }
  * { margin: 0; padding: 0; box-sizing: border-box; }
  html, body {
    width: 1200px;
    height: 209px;
    overflow: hidden;
    background: var(--bg);
    font-family: "Jost", sans-serif;
  }
  .site-footer {
    position: relative;
    width: 1200px;
    height: 209px;
  }
  .footer-cta {
    height: 102px;
    display: flex;
    align-items: center;
    justify-content: center;
    border-bottom: 1px solid var(--rule);
  }
  .footer-cta__link {
    display: flex;
    align-items: center;
    gap: 11px;
    color: var(--text-strong);
    text-decoration: none;
    font-size: 12.5px;
    font-weight: 500;
    letter-spacing: 0.3px;
  }
  .footer-bar {
    position: absolute;
    top: 103px;
    left: 0;
    width: 1200px;
    height: 106px;
  }
  .legal-links {
    position: absolute;
    left: 161px;
    top: 44px;
    display: flex;
    align-items: center;
    gap: 12px;
    font-size: 10.5px;
    font-weight: 300;
    color: var(--text-muted);
  }
  .legal-links a { color: inherit; text-decoration: none; }
  .dash {
    display: inline-block;
    width: 14px;
    height: 1px;
    background: var(--text-muted);
  }
  .brand {
    position: absolute;
    left: 0;
    right: 0;
    top: 40px;
    text-align: center;
    color: var(--text-strong);
    font-size: 16px;
    font-weight: 600;
    letter-spacing: 4px;
    padding-left: 4px;
  }
  .social {
    position: absolute;
    left: 823px;
    top: 49px;
    display: flex;
    align-items: center;
    gap: 8px;
  }
  .social__item {
    display: block;
    width: 12px;
    height: 12px;
    border-radius: 50%;
    background: var(--text-muted);
  }
  .social .dash { width: 13px; }
</style>
</head>
<body>
  <footer class="site-footer">
    <div class="footer-cta">
      <a class="footer-cta__link" href="#">
        Privacy Collection Statements
        <svg width="12" height="10" viewBox="0 0 12 10" aria-hidden="true">
          <path d="M0 5.5h10M6.5 1.5L10.5 5.5 6.5 9.5" fill="none" stroke="#ffffff" stroke-width="1.8"/>
        </svg>
      </a>
    </div>
    <div class="footer-bar">
      <nav class="legal-links">
        <a href="#">Terms Of Use &amp; Privacy Policy</a>
        <span class="dash"></span>
        <a href="#">Costumer Care</a>
      </nav>
      <div class="brand">PELORIS</div>
      <nav class="social" aria-label="Social channels">
        <a class="social__item" href="#" aria-label="Social channel 1"></a>
        <span class="dash"></span>
        <a class="social__item" href="#" aria-label="Social channel 2"></a>
        <span class="dash"></span>
        <a class="social__item" href="#" aria-label="Social channel 3"></a>
        <span class="dash"></span>
        <a class="social__item" href="#" aria-label="Social channel 4"></a>
        <span class="dash"></span>
        <a class="social__item" href="#" aria-label="Social channel 5"></a>
      </nav>
    </div>
  </footer>
</body>
</html>
```